Designing our 2018 Look Book! New help with slide design and picture layout

We create a yearly "Look book" with all of our season's designs for the year and need creative help creating the design and layout of the book

Need help with the slide design and picture layout

Target Market(s)

Property managers and office managers

Requirements
Must have
• layout of the photos and design of cover slide templates
• See our logo attached (color scheme and you can use the logo as well)
• Also see our website for our "look" www.dornhive.com

```html
<!DOCTYPE html>
<html lang="en">
<head>
<meta charset="utf-8">
<title>Dornhive Look Book 2018 – Cover Slide</title>
<link rel="stylesheet" href="https://fonts.googleapis.com/css2?family=Cormorant+Garamond:wght@500;600&display=swap">
<style>
  :root {
    --paper: #ffffff;
    --forest: #212d28;
    --leaf: #6aa538;
    --leaf-mid: #4e9a3c;
    --leaf-light: #78b84a;
    --leaf-deep: #2f8a3c;
    --leaf-dark: #1f4a1c;
    --olive: #6b8a14;
    --teal: #2bc0b4;
    --teal-soft: #c6eeea;
    --mist: #aeb6b6;
    --photo-green: #3f8d4a;
    --photo-shade: #2c4a3c;
  }
  * { margin: 0; padding: 0; box-sizing: border-box; }
  html, body { width: 1200px; height: 848px; overflow: hidden; background: var(--paper); }
  .cover { position: relative; width: 1200px; height: 848px; overflow: hidden; background: var(--paper); }
  .cover-art { position: absolute; inset: 0; }
  .headline-strip {
    position: absolute; left: 397px; top: 560px; width: 680px; height: 56px;
    background: linear-gradient(90deg, rgba(255,255,255,0.96) 0%, rgba(255,255,255,0.92) 60%, rgba(255,255,255,0) 100%);
  }
  .headline {
    position: absolute; left: 436px; top: 559px; height: 58px; line-height: 58px;
    font-family: "Cormorant Garamond", Georgia, serif; font-weight: 600;
    font-size: 49px; letter-spacing: 1px; color: var(--olive); white-space: nowrap;
  }
  .footer-band { position: absolute; left: 0; top: 655px; width: 1200px; height: 193px; background: var(--forest); overflow: hidden; }
  .brand-echo {
    position: absolute; left: 330px; top: 20px; white-space: nowrap;
    font-family: "Cormorant Garamond", Georgia, serif; font-weight: 600;
    font-size: 260px; line-height: 1; color: var(--leaf-dark);
  }
  .brand-mark { position: absolute; left: 1024px; top: 668px; width: 60px; height: 60px; border-radius: 50%; background: var(--leaf); }
  .brand-name {
    position: absolute; left: 780px; top: 718px; white-space: nowrap;
    font-family: "Cormorant Garamond", Georgia, serif; font-weight: 600;
    font-size: 98px; line-height: 1; color: var(--leaf);
  }
  .feature-photo {
    position: absolute; left: 103px; top: 472px; width: 280px; height: 280px; border-radius: 50%;
    border: 7px solid var(--paper);
    background: radial-gradient(circle at 40% 35%, #4f9a3e 0%, #3c7a34 40%, #6f7a78 75%, #9aa0a6 100%);
    box-shadow: 4px 8px 10px rgba(0,0,0,0.55);
  }
</style>
</head>
<body>
<main class="cover">
  <svg class="cover-art" viewBox="0 0 1200 848" width="1200" height="848">
    <defs>
      <linearGradient id="office-photo-tone" x1="0" y1="0" x2="1" y2="1">
        <stop offset="0" stop-color="#6fa89a"/>
        <stop offset="0.45" stop-color="var(--photo-green)"/>
        <stop offset="1" stop-color="var(--photo-shade)"/>
      </linearGradient>
      <linearGradient id="teal-swoosh-tone" x1="0" y1="0" x2="1" y2="1">
        <stop offset="0" stop-color="var(--teal-soft)"/>
        <stop offset="0.55" stop-color="var(--teal)" stop-opacity="0.75"/>
        <stop offset="1" stop-color="var(--teal-soft)"/>
      </linearGradient>
      <linearGradient id="teal-corner-tone" x1="0" y1="0" x2="0" y2="1">
        <stop offset="0" stop-color="var(--teal)" stop-opacity="0.55"/>
        <stop offset="1" stop-color="var(--teal-soft)" stop-opacity="0.6"/>
      </linearGradient>
      <linearGradient id="mist-swoosh-tone" x1="0" y1="0" x2="1" y2="0">
        <stop offset="0" stop-color="var(--mist)" stop-opacity="0"/>
        <stop offset="0.5" stop-color="var(--mist)" stop-opacity="0.55"/>
        <stop offset="1" stop-color="var(--mist)" stop-opacity="0.1"/>
      </linearGradient>
      <linearGradient id="teal-ribbon-tone" x1="0" y1="0" x2="1" y2="0">
        <stop offset="0" stop-color="var(--teal-soft)"/>
        <stop offset="0.7" stop-color="var(--teal-soft)"/>
        <stop offset="1" stop-color="var(--teal-soft)" stop-opacity="0"/>
      </linearGradient>
    </defs>

    <path class="teal-corner" role="img" aria-label="Fine teal line-work swoosh pattern" d="M1090 0 H1200 V130 C1120 230 1010 300 900 330 C1020 240 1070 130 1090 0 Z" fill="url(#teal-corner-tone)"/>
    <path class="teal-swoosh" role="img" aria-label="Fine teal line-work swoosh pattern" d="M740 0 H1090 C1060 150 960 290 820 365 C760 395 690 410 610 400 C700 330 740 200 740 0 Z" fill="url(#teal-swoosh-tone)"/>
    <path class="mist-swoosh" role="img" aria-label="Fine grey line-work swoosh pattern" d="M600 475 C700 405 850 395 1010 420 C880 425 740 445 600 475 Z" fill="url(#mist-swoosh-tone)"/>
    <rect class="teal-ribbon" x="420" y="615" width="560" height="40" fill="url(#teal-ribbon-tone)"/>

    <path class="photo-band" d="M0 0 H800 C780 260 660 470 470 540 C330 580 160 560 0 505 Z" fill="var(--leaf)"/>
    <path role="img" aria-label="Photo: office meeting room with large potted plants in front of tall windows" class="office-photo" d="M0 0 H760 C740 250 620 440 440 500 C320 535 160 520 0 478 Z" fill="url(#office-photo-tone)"/>

    <path class="leaf-sweep" d="M1200 270 C1000 300 860 430 817 655 H1200 Z" fill="var(--leaf-mid)" opacity="0.95"/>
    <path class="leaf-sweep-deep" d="M1200 360 C1060 400 960 500 920 655 H1200 Z" fill="var(--leaf-deep)" opacity="0.45"/>
    <path class="leaf-sweep-light" d="M1200 450 C1090 480 1000 560 960 655 H1200 Z" fill="var(--leaf-light)" opacity="0.8"/>
  </svg>

  <div class="headline-strip"></div>
  <h1 class="headline">INSERT TEXT HERE</h1>

  <section class="footer-band">
    <span class="brand-echo" aria-hidden="true">Dornhive</span>
  </section>
  <div class="feature-photo" role="img" aria-label="Photo: lounge with a living green plant wall, pendant lights and white sofas"></div>
  <span class="brand-mark" aria-hidden="true"></span>
  <p class="brand-name">Dornhive</p>
</main>
</body>
</html>
```